Green Logistics / Last Mile Delivery Firm needs cool one-page website

FYI - We do have a detailed brief in the uploaded files section below
COMPANY
We recently launched the company Brook Logistics which is a pioneer in urban green logistics and provides zero-emissions last mile delivery services (i.e. delivery of parcels with delivery vans to the doorstep of households) for its logistics and retail clients.
We take on urban parcel delivery for our clients with a 100% electric commercial vehicles fleet, fair and sustainable working conditions for our employees and an unparalleled professional and customer-focused mindset.
WEBSITE
In the detailed brief, we have provided examples to emulate. We need the design + coding of the website. Website needs to be friendly/optimized for and should open swiftly on both Android & iOS.
In general, the website should convey
- green mission of the company
- sustainability (good working conditions, focus on employees)
- customer orientation
- professionalism
DESIGN
In the detailed brief, we have provided designs to emulate.
Color design: we do have a logo which features 2 green colors (one lighter and one darker color tone). However, the colors on the website do not necessarily need to follow these 2 colors exactly as we are able to switch the logo colors.
Imagery: should reflect maybe 50% green/leaf/tree , 25% customer and employee orientation, and 25% logistics (here it's important that it is the last mile delivery, i.e. delivery with delivery vans to the doorstep of households)
Coding

```html
<!DOCTYPE html>
<html lang="en">
<head>
<meta charset="utf-8">
<title>Brook Logistics – Delivering parcels emissions-free</title>
<link href="https://fonts.googleapis.com/css2?family=Montserrat:wght@700;800&display=swap" rel="stylesheet">
<style>
  :root {
    --page-bg: #ffffff;
    --brand-green: #1f9a4a;
    --overlay-dark: #1e2c2f;
    --overlay-mid: #34484b;
    --text-light: #ffffff;
    --arrow-grey: #9aa3a5;
    --arrow-dark: #222a2c;
  }
  * { margin: 0; padding: 0; box-sizing: border-box; }
  html, body {
    width: 1200px; height: 1200px; overflow: hidden;
    background: var(--page-bg);
    font-family: "Montserrat", Arial, sans-serif;
  }
  .hero {
    position: absolute; left: 14px; top: 322px;
    width: 1171px; height: 553px; overflow: hidden;
  }
  .hero-photo {
    position: absolute; inset: 0;
    background:
      radial-gradient(ellipse at 62% 55%, #4a5e60 0%, transparent 55%),
      linear-gradient(180deg, var(--overlay-mid) 0%, #3b4f50 45%, var(--overlay-dark) 100%);
  }
  .brand {
    position: absolute; left: 110px; top: 34px;
    display: flex; align-items: center; gap: 10px;
    text-decoration: none;
  }
  .brand-mark {
    width: 34px; height: 34px; border-radius: 50%;
    background: var(--brand-green);
  }
  .brand-name {
    color: var(--text-light); font-weight: 700; font-size: 16px;
    line-height: 1;
  }
  .main-nav {
    position: absolute; left: 531px; top: 42px;
    display: flex; gap: 34px; list-style: none;
  }
  .main-nav a {
    color: var(--text-light); text-decoration: none;
    font-size: 12px; font-weight: 700; text-transform: uppercase;
    display: inline-block; padding-bottom: 6px;
  }
  .main-nav a.is-active { border-bottom: 2px solid var(--brand-green); }
  .main-nav .lang svg { margin-left: 4px; vertical-align: 1px; }
  .hero-title {
    position: absolute; left: 200px; top: 196px;
    color: var(--text-light); font-weight: 800; font-size: 44px;
    letter-spacing: -0.3px; white-space: nowrap;
  }
  .cta {
    position: absolute; left: 202px; top: 274px;
    width: 173px; height: 48px; border-radius: 24px;
    background: var(--brand-green); color: var(--text-light);
    font-size: 12px; font-weight: 700; text-transform: uppercase;
    display: flex; align-items: center; justify-content: center;
    text-decoration: none;
  }
  .slider-arrow {
    position: absolute; top: 283px; width: 52px; height: 52px;
    border-radius: 50%; display: flex; align-items: center; justify-content: center;
  }
  .slider-arrow.prev { left: 32px; background: var(--arrow-grey); }
  .slider-arrow.next { left: 1085px; background: var(--text-light); }
  .scroll-down { position: absolute; left: 574px; top: 508px; }
</style>
</head>
<body>
  <section class="hero">
    <div class="hero-photo" role="img" aria-label="Delivery driver carrying parcels beside an electric delivery van in a residential street, under a dark overlay"></div>

    <a href="#" class="brand">
      <span class="brand-mark"></span>
      <span class="brand-name">Brook Logistics</span>
    </a>

    <ul class="main-nav">
      <li><a href="#" class="is-active">Home</a></li>
      <li><a href="#">About</a></li>
      <li><a href="#">Services</a></li>
      <li><a href="#">Careers</a></li>
      <li><a href="#">Contact</a></li>
      <li><a href="#" class="lang">English<svg width="9" height="8" viewBox="0 0 9 8"><path d="M0 0h9L4.5 8z" fill="#fff"/></svg></a></li>
    </ul>

    <h1 class="hero-title">Delivering parcels emissions-free</h1>
    <a href="#" class="cta">Get started</a>

    <div class="slider-arrow prev" aria-label="Previous slide">
      <svg width="14" height="18" viewBox="0 0 14 18"><path d="M10 2L3 9l7 7" fill="none" stroke="#222a2c" stroke-width="3"/></svg>
    </div>
    <div class="slider-arrow next" aria-label="Next slide">
      <svg width="14" height="18" viewBox="0 0 14 18"><path d="M4 2l7 7-7 7" fill="none" stroke="#222a2c" stroke-width="3"/></svg>
    </div>

    <svg class="scroll-down" width="22" height="22" viewBox="0 0 22 22" aria-label="Scroll down">
      <path d="M4 3l7 7 7-7M4 11l7 7 7-7" fill="none" stroke="#fff" stroke-width="2.5"/>
    </svg>
  </section>
</body>
</html>
```